Revamp our wedding venue website

Currently we are using wordpress for our website and hoped to find a designer that can assist us with making the website prettier and more pleasing and draw more interest. www.velmarhall.com is our current site. We are connected to google business mail, so I would prefer to stay with this for now and update our gallery with new photos, blog page and putting the contact us form back on all the pages.

Target Market(s)

20-40 years of age, all ranges of styles and generally clients looking for a different modern feel vs. a hotel hall.

Industry/Entity Type

Wedding

Logo Text

1927 Velmar Hall

Number of Pages Required

4 page

Font styles to use
Serif

Requirements
Must have
• Light, airy feel. Romantic and informative. Mobile friendly and easy to contact us-preferred contact form on all pages. Gallery of photos. Previous reviews
Nice to have
• Bio of staff, maybe some videos, and fun things to do in the area for out of town guests. Maps and also venue blank floor plan.

```html
<!DOCTYPE html>
<html lang="en">
<head>
<meta charset="utf-8">
<title>1927 Velmar Hall — Weddings &amp; Events</title>
<link rel="stylesheet" href="https://fonts.googleapis.com/css2?family=Quicksand:wght@500;700&family=Crimson+Text:ital@0;1&family=Open+Sans:wght@400;600&display=swap">
<style>
:root{
  --yellow:#ffe100;
  --charcoal:#555555;
  --dark:#242424;
  --darker:#1a1a1a;
  --ink:#4a4a4a;
  --white:#ffffff;
  --band:#6b6b6b;
  --brick-light:#b39a7a;
  --brick:#8c7258;
  --brick-deep:#5e4a3a;
  --glass:#1f1d1c;
}
*{box-sizing:border-box;margin:0;padding:0}
html,body{width:1200px;height:2821px;overflow:hidden;background:var(--white)}
body{position:relative;font-family:"Quicksand",sans-serif}
.abs{position:absolute}

/* hero */
.hero-photo{left:0;top:0;width:1200px;height:626px;
  background:
    radial-gradient(ellipse 260px 220px at 590px 470px,rgba(245,240,235,.35) 0%,rgba(245,240,235,0) 100%),
    linear-gradient(180deg,var(--brick-light) 0%,var(--brick) 18%,var(--brick-deep) 32%,#3a322c 40%,var(--glass) 50%,#2a2522 68%,var(--brick-deep) 80%,#4a3c30 100%)}
.hero-shade{left:0;top:0;width:1200px;height:626px;background:linear-gradient(90deg,rgba(0,0,0,.25) 0%,rgba(0,0,0,0) 30%,rgba(0,0,0,0) 70%,rgba(0,0,0,.25) 100%)}
.site-bar{left:0;top:0;width:1200px;height:94px;background:rgba(60,60,60,.5)}
.brand{left:34px;top:22px;font-weight:700;font-size:32px;color:var(--white)}
.nav{left:0;top:23px;width:1200px;height:49px;font-weight:700;font-size:16px;color:var(--white)}
.nav a{color:inherit;text-decoration:none;position:absolute;top:0;height:49px;line-height:49px}
.nav .active{background:var(--yellow);width:111px;text-align:center}
.hero-title{left:0;top:272px;width:1200px;text-align:center;font-weight:700;font-size:54px;color:var(--white)}
.tagline-band{left:0;top:626px;width:1200px;height:85px;background:var(--band);border-top:3px dashed var(--yellow);border-bottom:3px dashed var(--yellow);display:flex;align-items:center;justify-content:center;font-family:"Crimson Text",serif;font-style:italic;font-weight:700;font-size:31px;color:var(--yellow)}

/* about */
.pearl-bg{left:0;top:730px;width:1200px;height:1029px;background:radial-gradient(ellipse at 85% 20%,#ffffff 0%,#eeeeee 40%,#e4e4e4 100%)}
.section-title{left:0;width:1200px;text-align:center;font-family:"Crimson Text",serif;font-style:italic;font-size:40px;color:var(--ink)}
.why-photo{left:417px;top:790px;width:290px;height:225px;
  background:
    radial-gradient(ellipse 48% 50% at 50% 45%,rgba(60,60,60,.9) 0%,rgba(110,110,110,.85) 40%,rgba(170,170,170,.6) 70%,rgba(235,235,235,0) 100%),
    linear-gradient(90deg,rgba(90,90,90,.35),rgba(200,200,200,.2),rgba(90,90,90,.35));
  -webkit-mask-image:radial-gradient(ellipse 55% 55% at 50% 45%,#000 60%,transparent 100%);
  mask-image:radial-gradient(ellipse 55% 55% at 50% 45%,#000 60%,transparent 100%)}
.why-text{left:66px;top:1012px;width:1068px;text-align:center;font-family:"Crimson Text",serif;font-style:italic;font-size:23px;line-height:32px;color:#555}
.divider-line{top:1222px;height:3px;background:linear-gradient(180deg,#9aa6b8,#3a4a6a)}
.divider-mark{left:508px;top:1206px;width:184px;height:34px;background:linear-gradient(90deg,#5a6a88,#2f3e5c,#5a6a88);border-radius:17px;opacity:.55}

/* testimonials */
.card{top:1318px;width:304px;height:350px;background:var(--charcoal);color:var(--white);text-align:center}
.card.featured{background:var(--yellow);color:var(--charcoal)}
.avatar{position:absolute;left:92px;top:15px;width:120px;height:120px;border-radius:50%;border:6px solid var(--white);background:radial-gradient(circle at 50% 60%,#e89a3c 0%,#c0601c 45%,#1a1a1a 80%)}
.card .rule{position:absolute;left:92px;top:138px;width:120px;height:3px;background:var(--white)}
.card.featured .rule{background:var(--charcoal)}
.quote{position:absolute;left:24px;top:162px;width:256px;font-weight:700;font-size:17.5px;line-height:22px}
.client{position:absolute;left:0;width:304px;top:290px;font-weight:700;font-size:17px;color:var(--yellow)}
.card.featured .client{color:var(--charcoal)}
.arrow{top:1456px}

/* enquiry */
.contact-photo{left:0;top:1759px;width:1200px;height:479px;background:linear-gradient(180deg,#1c1c1c 0%,#2a2826 50%,#3a3430 100%)}
.contact-copy{left:53px;top:1796px;width:510px;font-weight:700;font-size:23.5px;line-height:32px;color:var(--white)}
.contact-copy .hl{color:var(--yellow)}
.learn-more{left:62px;top:2045px;font-weight:700;font-size:25px;color:var(--yellow)}
.enquire-box{left:786px;top:1806px;width:358px;height:363px;border:4px solid #8a7a1a;background:rgba(30,30,30,.6)}
.enquire-head{left:831px;top:1840px;width:294px;height:41px;background:var(--yellow);color:var(--white);font-weight:700;font-size:28px;text-align:center;line-height:41px}
.field-label{left:820px;width:66px;text-align:right;font-weight:700;font-size:16.5px;color:var(--white)}
.field{left:892px;width:231px;height:41px;background:var(--white);font-family:"Quicksand",sans-serif;font-weight:500;font-size:16px;color:#444;padding-left:12px;line-height:41px}
.quote-btn{left:903px;top:2084px;width:165px;height:53px;border-radius:27px;border:4px solid var(--yellow);background:var(--white);font-weight:700;font-size:17px;color:#444;text-align:center;line-height:45px}

/* location */
.location{left:0;top:2238px;width:1200px;height:160px;text-align:center;font-family:"Open Sans",sans-serif;font-size:27px;line-height:33px;color:#555;padding-top:30px;font-style:normal}
.comment-band{left:0;top:2398px;width:1200px;height:113px;background:var(--yellow)}
.comment-input{left:213px;top:2428px;width:526px;height:55px;background:var(--white)}
.comment-btn{left:754px;top:2428px;width:192px;height:55px;background:var(--charcoal);color:var(--white);font-family:"Open Sans",sans-serif;font-size:26px;text-align:center;line-height:55px}

/* footer */
.footer{left:0;top:2511px;width:1200px;height:245px;background:var(--dark)}
.footer-brand{left:0;top:2567px;width:1200px;text-align:center;font-weight:700;font-size:34px;color:var(--white)}
.footer-nav{left:0;top:2680px;width:1200px;text-align:center;font-weight:700;font-size:34px;color:var(--white)}
.footer-nav span{margin:0 9px}
.footer-nav .active{color:var(--yellow)}
.copyright{left:0;top:2756px;width:1200px;height:65px;background:var(--darker);text-align:center;line-height:65px;font-weight:700;font-size:18px;color:var(--white);letter-spacing:-.5px}
.copyright .hl{color:var(--yellow)}
</style>
</head>
<body>

<header>
  <div class="abs hero-photo" role="img" aria-label="Bride and groom kissing in front of the brick venue facade"></div>
  <div class="abs hero-shade"></div>
  <div class="abs site-bar"></div>
  <div class="abs brand">1927 Velmar Hall</div>
  <nav class="abs nav">
    <a class="active" style="left:536px">Home</a>
    <a style="left:658px">Weddings</a>
    <a style="left:779px">Events</a>
    <a style="left:874px">Catering</a>
    <a style="left:974px">Gallery</a>
    <a style="left:1070px">Contact Us</a>
  </nav>
  <h1 class="abs hero-title">Weddings &amp; Events</h1>
  <div class="abs tagline-band">Imagine your wedding or event in Tampa´s premiere, unique and historic venue</div>
</header>

<main>
  <div class="abs pearl-bg" role="img" aria-label="Soft white pearl strands background"></div>
  <h2 class="abs section-title" style="top:736px;font-weight:400">Why 1927 Velmar Hall</h2>
  <div class="abs why-photo" role="img" aria-label="Black and white photo of a couple at the ceremony"></div>
  <p class="abs why-text">When choosing the location for your wedding or event, the 1927 Velmar Hall provides you with an all-inclusive experience, from the moment you arrive, through the creative food, and amazing photo opportunities. The unique open-kitchen provides you, and your guests a front-row seat to our creative, and talented chefs, as they prepare a culinary experience like no other. The full, and spacious bar, serves up wonderful libations and specialty cocktails that enhance your experience.</p>

  <div class="abs divider-line" style="left:40px;width:456px"></div>
  <div class="abs divider-line" style="left:704px;width:452px"></div>
  <div class="abs divider-mark" role="img" aria-label="Flourish ornament"></div>
  <h2 class="abs section-title" style="top:1244px;font-weight:400">Testimonials</h2>

  <svg class="abs arrow" style="left:0" width="66" height="78" viewBox="0 0 66 78"><polygon points="66,0 66,78 0,39" fill="#555"/></svg>
  <svg class="abs arrow" style="left:1126px" width="66" height="78" viewBox="0 0 66 78"><polygon points="0,0 0,78 66,39" fill="#555"/></svg>

  <article class="abs card" style="left:70px">
    <div class="avatar" role="img" aria-label="Couple silhouette portrait"></div>
    <div class="rule"></div>
    <p class="quote">It’s been almost a month since my wedding at the Velmar Hall and I am still with my mouth open, it was absolutely beautiful.</p>
    <p class="client">Marisa &amp; Owen, Tampa, FL</p>
  </article>
  <article class="abs card featured" style="left:436px">
    <div class="avatar" role="img" aria-label="Couple silhouette portrait"></div>
    <div class="rule"></div>
    <p class="quote">It’s been almost a month since my wedding at the Velmar Hall and I am still with my mouth open, it was absolutely beautiful.</p>
    <p class="client">Marisa &amp; Owen, Tampa, FL</p>
  </article>
  <article class="abs card" style="left:813px">
    <div class="avatar" role="img" aria-label="Couple silhouette portrait"></div>
    <div class="rule"></div>
    <p class="quote">It’s been almost a month since my wedding at the Velmar Hall and I am still with my mouth open, it was absolutely beautiful.</p>
    <p class="client">Marisa &amp; Owen, Tampa, FL</p>
  </article>

  <section>
    <div class="abs contact-photo" role="img" aria-label="Wedding party gathered on a street at dusk"></div>
    <p class="abs contact-copy">Want to find out more about having your wedding or event here at the beautiful, historic <span class="hl">1927 Velmar Hall</span>, call or contact our wedding and event specialists today, to check date availability, and to arrange your personal tour 555.014.2790, Events@VelmarHall.com</p>
    <div class="abs learn-more">Learn More</div>

    <div class="abs enquire-box"></div>
    <div class="abs enquire-head">ENQUIRE</div>
    <div class="abs field-label" style="top:1901px">Name</div>
    <div class="abs field" style="top:1893px">jamie carter</div>
    <div class="abs field-label" style="top:1950px">Email</div>
    <div class="abs field" style="top:1942px">abc@xyz.com</div>
    <div class="abs field-label" style="top:1997px">Date</div>
    <div class="abs field" style="top:1989px">12-20-2015</div>
    <div class="abs field-label" style="top:2044px">Type</div>
    <div class="abs field" style="top:2036px">wedding or event</div>
    <div class="abs quote-btn">Get Quote</div>
  </section>

  <address class="abs location">We’re conveniently located in historic Harbor Quarter at:<br>1927 East 9th Ave.<br>Tampa, FL 33605</address>

  <div class="abs comment-band"></div>
  <div class="abs comment-input"></div>
  <div class="abs comment-btn">Comment</div>
</main>

<footer>
  <div class="abs footer"></div>
  <div class="abs footer-brand">1927 Velmar Hall</div>
  <nav class="abs footer-nav"><span class="active">Home</span><span>Weddings</span><span>Events</span><span>Catering</span><span>Gallery</span><span>Contact Us</span></nav>
  <div class="abs copyright">COPYRIGHT@<span class="hl">1927VELMARHALL.COM</span>.ALL RIGHTS RESERVED</div>
</footer>

</body>
</html>
```